Velmora Business Card Design Project

Need a design for Velmora business cards
Square rounded corner card:
http://www.printquilt.example/25-X-25-Rounded-Corner-Business-Cards_p_204.html
Front content (specific example is used to establish format):
Colm Harwick
Founder
650-555-0182
colm@velmora.com
@colmjharwick
www.velmora.com
Back content:
Vertical velmora logo (white on red)
https://www.filecove.example/sh/kq4hlwtnexg31rb/QQWmzr5P714Lk2fJvX3aTnH7c?dl=0
Target Market(s)
Young professionals (early 20's)
Industry/Entity Type
Business
Requirements
Must have
- Look similar to
http://storage.artmarket.example/design_img/413907/52210/52210_9182634_413907_image.jpg
Adapted to square rounded corner format

```html
<!DOCTYPE html>
<html lang="en">
<head>
<meta charset="utf-8">
<title>Velmora Business Cards</title>
<link rel="stylesheet" href="https://fonts.googleapis.com/css2?family=Montserrat:wght@400;500;600&display=swap">
<style>
  :root {
    --backdrop: #e2e2e2;
    --card: #ffffff;
    --brand-red: #dc261f;
    --ink: #222222;
  }
  html, body {
    margin: 0;
    padding: 0;
    overflow: hidden;
  }
  body {
    width: 1200px;
    height: 875px;
    background: var(--backdrop);
    position: relative;
    font-family: "Montserrat", Arial, sans-serif;
  }
  .card {
    position: absolute;
    top: 245px;
    width: 384px;
    height: 384px;
    background: var(--card);
    border-radius: 14px;
  }
  .card--front { left: 191px; }
  .card--back { left: 625px; }

  .brand {
    position: absolute;
    display: flex;
    align-items: center;
    color: var(--brand-red);
    font-weight: 500;
    letter-spacing: 1px;
  }
  .brand__mark {
    background: var(--brand-red);
    flex: none;
  }
  .card--front .brand {
    left: 54px;
    top: 52px;
    font-size: 38px;
    gap: 14px;
  }
  .card--front .brand__mark {
    width: 34px;
    height: 34px;
  }

  .contact {
    position: absolute;
    left: 0;
    right: 0;
    top: 168px;
    text-align: center;
    color: var(--ink);
    font-size: 19px;
    line-height: 27px;
  }
  .contact__name { color: var(--brand-red); }
  .contact__role { margin-bottom: 23px; }
  .contact__site-name { color: var(--brand-red); }

  .card--back .brand {
    left: 0;
    right: 0;
    top: 78px;
    flex-direction: column;
    gap: 34px;
    font-size: 42px;
  }
  .card--back .brand__mark {
    width: 130px;
    height: 130px;
  }
</style>
</head>
<body>
  <section class="card card--front">
    <div class="brand">
      <span class="brand__mark"></span>
      <span class="brand__name">velmora</span>
    </div>
    <div class="contact">
      <div class="contact__name">Colm Harwick</div>
      <div class="contact__role">founder</div>
      <div class="contact__phone">650-555-0182</div>
      <div class="contact__email">colm@velmora.com</div>
      <div class="contact__handle">@colmjharwick</div>
      <div class="contact__site">www.<span class="contact__site-name">velmora</span>.com</div>
    </div>
  </section>

  <section class="card card--back">
    <div class="brand">
      <span class="brand__name">velmora</span>
      <span class="brand__mark"></span>
    </div>
  </section>
</body>
</html>
```